Business Cards for Tax Preparation Business
KRT Tax Preparation
Business Cards for Tax Preparation Business - Financial Services
Creative Brief
Cutting-Edge
Brian K Holloway
Registered Tax Return Preparer
47 Birchmont Avenue, Suite 318 West Hartford, CT 06107
860-555-0148 x36
brian@krtfiling.example
www.krtfiling.example

```html
<!DOCTYPE html>
<html lang="en">
<head>
<meta charset="utf-8">
<title>KRT Tax Preparation – Stationery</title>
<link href="https://fonts.googleapis.com/css2?family=Libre+Baskerville:wght@400;700&family=Open+Sans:wght@400;600&display=swap" rel="stylesheet">
<style>
:root{
  --bg:#e9eaec;
  --paper:#ffffff;
  --navy:#1f3f9e;
  --blue:#2447b8;
  --blue-dark:#162f86;
  --gold:#c9a227;
  --gold-light:#f0d774;
  --ink:#4a4a4a;
  --muted:#8a8a8a;
}
*{margin:0;padding:0;box-sizing:border-box}
html,body{width:1200px;height:936px;overflow:hidden}
body{background:var(--bg);position:relative;font-family:"Open Sans",Arial,sans-serif;color:var(--ink)}
.piece{position:absolute;background:var(--paper)}
.brand{font-family:"Libre Baskerville",Georgia,serif;font-weight:700;color:var(--navy);text-align:center;line-height:1.1;display:flex;align-items:center;justify-content:center;gap:8px}
.brand-mark{display:inline-block;background:var(--gold);flex:none}
.footer-band{position:absolute;left:0;right:0;display:flex;align-items:center}
.gold-rule{flex:1;height:3px;background:linear-gradient(90deg,var(--gold),var(--gold-light),var(--gold))}
.blue-strip{background:linear-gradient(90deg,var(--blue-dark),var(--blue),var(--blue-dark));color:#fff;text-align:center}

/* Letterhead */
.letterhead{left:248px;top:56px;width:320px;height:538px}
.letterhead .brand{position:absolute;top:26px;left:0;right:0;font-size:15px}
.letterhead .brand-mark{width:10px;height:10px}
.letter-body{position:absolute;top:82px;left:28px;right:28px;font-size:5.6px;line-height:1.6;color:var(--ink)}
.letter-body p{margin-bottom:8px}
.letter-sign{margin-top:22px}
.letterhead .footer-band{bottom:22px}
.letterhead .blue-strip{width:150px;height:10px}
.letter-contact{position:absolute;bottom:36px;left:0;right:0;text-align:center;font-size:4.6px;color:var(--muted)}
.letterhead .web{position:absolute;bottom:10px;left:0;right:0;text-align:center;font-size:5px;color:var(--navy)}

/* Folder */
.folder{left:635px;top:51px;width:404px;height:579px}
.folder .brand{position:absolute;top:250px;left:0;right:0;font-size:30px;flex-direction:row}
.folder .brand-mark{width:18px;height:18px}
.folder .footer-band{bottom:30px}
.folder .blue-strip{width:200px;height:20px;font-size:8px;line-height:20px}

/* Business cards */
.card{left:225px;width:185px;height:100px}
.card-front{top:678px}
.card-front .brand{position:absolute;top:14px;left:0;right:0;font-size:12px}
.card-front .brand-mark{width:8px;height:8px}
.card-front .blue-strip{position:absolute;top:50px;left:0;right:0;height:12px;font-size:5px;line-height:12px}
.card-front .details{position:absolute;top:68px;left:0;right:0;text-align:center;font-size:5px;line-height:1.5;color:var(--ink)}
.card-back{top:783px;background:linear-gradient(135deg,var(--blue),var(--blue-dark))}
.card-back .brand{position:absolute;inset:0;color:#fff;font-size:14px}
.card-back .brand-mark{width:9px;height:9px}

/* Envelopes */
.envelope{top:691px;height:205px}
.envelope-open{left:448px;width:333px}
.envelope-open .brand{position:absolute;top:18px;left:18px;font-size:10px;justify-content:flex-start}
.envelope-open .brand-mark{width:7px;height:7px}
.envelope-open .return{position:absolute;top:40px;left:18px;font-size:5px;line-height:1.5;color:var(--muted)}
.envelope-open .footer-band{bottom:14px}
.envelope-open .blue-strip{width:140px;height:9px;font-size:4.8px;line-height:9px}
.envelope-flap{left:814px;width:312px}
.envelope-flap svg{position:absolute;inset:0}
.envelope-flap .brand{position:absolute;top:40px;left:0;right:0;font-size:11px}
.envelope-flap .brand-mark{width:7px;height:7px}
</style>
</head>
<body>

<section class="piece letterhead">
  <div class="brand"><span class="brand-mark"></span>KRT Tax Preparation</div>
  <div class="letter-body">
    <p>June 4, 2025</p>
    <p>Dear Client,<br>47 Birchmont Avenue, Suite 318 West Hartford, CT 06107</p>
    <p>Your tax documents for the current year have been received and reviewed by our office.</p>
    <p>We have prepared your return and summarised the key figures for your records. Please review each page carefully before signing.</p>
    <p>Should you have any questions about deductions, credits or filing deadlines, contact us directly and we will respond promptly.</p>
    <p>Best Regards,</p>
    <p class="letter-sign">Brian K Holloway<br>Registered Tax Return Preparer</p>
  </div>
  <div class="letter-contact">47 Birchmont Avenue, Suite 318 West Hartford, CT 06107 &nbsp;|&nbsp; 860-555-0148 x36 &nbsp;|&nbsp; brian@krtfiling.example</div>
  <div class="footer-band"><span class="gold-rule"></span><span class="blue-strip"></span><span class="gold-rule"></span></div>
  <div class="web">www.krtfiling.example</div>
</section>

<section class="piece folder">
  <div class="brand"><span class="brand-mark"></span>KRT Tax Preparation</div>
  <div class="footer-band"><span class="gold-rule"></span><span class="blue-strip">www.krtfiling.example</span><span class="gold-rule"></span></div>
</section>

<section class="piece card card-front">
  <div class="brand"><span class="brand-mark"></span>KRT Tax Preparation</div>
  <div class="blue-strip">Brian K Holloway · Registered Tax Return Preparer</div>
  <div class="details">860-555-0148 x36 · brian@krtfiling.example<br>www.krtfiling.example</div>
</section>

<section class="piece card card-back">
  <div class="brand"><span class="brand-mark"></span>KRT Tax Preparation</div>
</section>

<section class="piece envelope envelope-open">
  <div class="brand"><span class="brand-mark"></span>KRT Tax Preparation</div>
  <div class="return">47 Birchmont Avenue, Suite 318<br>West Hartford, CT 06107<br>860-555-0148 x36</div>
  <div class="footer-band"><span class="gold-rule"></span><span class="blue-strip">www.krtfiling.example</span><span class="gold-rule"></span></div>
</section>

<section class="piece envelope envelope-flap">
  <svg width="312" height="205" viewBox="0 0 312 205"><path d="M0 0 L156 92 L312 0" fill="none" stroke="#d8d9dc" stroke-width="1.2"/></svg>
  <div class="brand"><span class="brand-mark"></span>KRT Tax Preparation</div>
</section>

</body>
</html>
```